Book cover for ebook and Physical book for Mind Clutter Collective

I run a non-profit Mind Clutter Collective and I have a new book that needs a cover. For the physical book, I will need a full wrap. The mission is to help individuals Quiet the cycle of restless worry patterns. This book is title is "Quiet the cycle of restless worry patterns", and subtitle "Clear Your Mind of Static Noise." I am open to anything design wise, nothing is set in stone. Oh, MCC is pending Trademark.

Target Market(s)

Typically it's Mom's from 25-40

Industry/Entity Type

Mental Health

Font styles to use
Serif

Colors
f37122
9bcb3b
fbed22
0255a3
e34197

Requirements
Must have
• I do like simplicity, yet vibrant colors.
Nice to have
• The authors are Rex T. Whitford, and Dana Okonkwo. For some inspiration individuals refer to me as the Wonder Guide having reversed five incurable diseases.
Should not have
• The cover shouldn't be too busy.

```html
<!DOCTYPE html>
<html lang="en">
<head>
<meta charset="utf-8">
<title>Quiet the cycle of restless worry patterns — Cover and Spine</title>
<link rel="stylesheet" href="https://fonts.googleapis.com/css2?family=Jost:ital,wght@0,500;0,600;0,700;1,600&display=swap">
<style>
  :root {
    --backdrop: #e4e5e1;
    --cover-green: #b3d66a;
    --brand-pink: #e34197;
    --brand-blue: #0255a3;
    --brand-yellow: #fbed22;
    --brand-orange: #f37122;
    --white: #ffffff;
  }
  * { box-sizing: border-box; margin: 0; padding: 0; }
  html, body {
    width: 1200px;
    height: 854px;
    overflow: hidden;
    background: var(--backdrop);
    font-family: "Jost", "Century Gothic", sans-serif;
  }
  .canvas {
    position: relative;
    width: 1200px;
    height: 854px;
  }

  /* Front cover */
  .front-cover {
    position: absolute;
    left: 312px;
    top: 238px;
    width: 369px;
    height: 525px;
    background: var(--cover-green);
    overflow: hidden;
  }
  .dot {
    position: absolute;
    border-radius: 50%;
  }
  .dot--yellow { width: 72px; height: 72px; left: 252px; top: -51px; background: var(--brand-yellow); }
  .dot--blue   { width: 72px; height: 72px; left: -58px; top: 74px;  background: var(--brand-blue); }
  .dot--orange { width: 70px; height: 70px; left: 351px; top: 427px; background: var(--brand-orange); }

  .cover-title {
    position: absolute;
    left: 70px;
    top: 61px;
    width: 260px;
    color: var(--brand-pink);
    font-weight: 700;
    font-size: 26px;
    line-height: 27px;
    letter-spacing: 0.1px;
  }
  .title-rule {
    position: absolute;
    left: 71px;
    top: 155px;
    width: 229px;
    height: 2px;
    background: var(--white);
  }
  .cover-subtitle {
    position: absolute;
    left: 70px;
    top: 170px;
    color: var(--brand-pink);
    font-style: italic;
    font-weight: 600;
    font-size: 13px;
  }
  .cover-authors {
    position: absolute;
    left: 70px;
    top: 445px;
    color: var(--brand-blue);
    font-weight: 600;
    font-size: 21px;
    line-height: 21px;
  }

  /* Spine */
  .spine {
    position: absolute;
    left: 830px;
    top: 240px;
    width: 70px;
    height: 523px;
    background: var(--cover-green);
    overflow: hidden;
  }
  .spine-badge {
    position: absolute;
    left: -7px;
    top: 66px;
    width: 84px;
    height: 84px;
    border-radius: 50%;
    background: var(--brand-blue);
  }
  .spine-authors {
    position: absolute;
    left: 26px;
    top: 72px;
    height: 72px;
    writing-mode: vertical-rl;
    transform: rotate(180deg);
    color: var(--white);
    font-weight: 500;
    font-size: 10px;
    line-height: 11px;
    text-align: center;
  }
  .spine-title {
    position: absolute;
    left: 27px;
    top: 198px;
    height: 302px;
    writing-mode: vertical-rl;
    transform: rotate(180deg);
    color: var(--brand-pink);
    font-weight: 700;
    font-size: 13.5px;
    white-space: nowrap;
  }
</style>
</head>
<body>
<main class="canvas">
  <section class="front-cover" aria-label="Front cover">
    <span class="dot dot--yellow"></span>
    <span class="dot dot--blue"></span>
    <span class="dot dot--orange"></span>

    <h1 class="cover-title">Quiet the cycle of restless worry patterns</h1>
    <span class="title-rule"></span>
    <p class="cover-subtitle">Clear Your Mind of Static Noise</p>

    <p class="cover-authors">Rex T. Whitford<br>Dana Okonkwo</p>
  </section>

  <section class="spine" aria-label="Spine">
    <span class="spine-badge"></span>
    <p class="spine-authors">Rex T. Whitford<br>Dana Okonkwo</p>
    <p class="spine-title">Quiet the cycle of restless worry patterns</p>
  </section>
</main>
</body>
</html>
```